New Business Cards for NYC Salon

We are updating all of our cards. 7142-2869-4057 is my account number. We put names of our stylists on their cards. The back should include appointment space. Were looking for something more sleek and modern. Black/White Silver... or even touches of the orange color on our website which has been our thing for years. The design should communicate professional upscale boutique salon for men and women. Should be able to incorporate design into thank you cards, referral cards, brochure and postcards. The file is a zip file...we like the stacked ones black or white or the side versions.

Industry/Entity Type

Beauty Salon

Contact Information for Business Card

Marcus Dell's Salon313 W. 53rd Street, New York NY 10019 212-386-7714 info@marcusdellsalon.example www.marcusdellsalon.example

Font styles to use
Other font styles liked:
• trajan

Requirements
Must have
• we print a different card for every person in the salon. Begin by designing with the name Marcus. We will change it with every employee when printing. Must have a space for appointment date and time.
Nice to have
• Were looking to move towards the stacked or side placed logo but not opposed to utilizing the circular.
Should not have
• Photos

```html
<!DOCTYPE html>
<html lang="en">
<head>
<meta charset="utf-8">
<title>Marcus Dell's Salon — Business Cards</title>
<link rel="stylesheet" href="https://fonts.googleapis.com/css2?family=Cinzel:wght@400;500&display=swap">
<style>
  :root {
    --page: #e6e4e3;
    --card: #ffffff;
    --ink: #1a1a1a;
    --rule: #6d6d6d;
    --ornament-a: #ececec;
    --ornament-b: #f8f8f8;
    --shadow: rgba(0, 0, 0, 0.18);
  }
  * { box-sizing: border-box; margin: 0; padding: 0; }
  html, body {
    width: 1200px;
    height: 800px;
    overflow: hidden;
    background: var(--page);
  }
  .canvas {
    width: 1200px;
    height: 800px;
    display: flex;
    align-items: center;
    justify-content: center;
    gap: 60px;
  }
  .card {
    position: relative;
    width: 525px;
    height: 300px;
    background: var(--card);
    box-shadow: 0 10px 30px var(--shadow);
    font-family: "Cinzel", serif;
    color: var(--ink);
    overflow: hidden;
  }
  .ornament {
    position: absolute;
    width: 200px;
    height: 110px;
  }
  .ornament--top-left {
    top: 0; left: 0;
    background: radial-gradient(ellipse at top left, var(--ornament-a) 0%, var(--ornament-b) 55%, transparent 80%);
  }
  .ornament--bottom-right {
    right: 0; bottom: 0;
    background: radial-gradient(ellipse at bottom right, var(--ornament-a) 0%, var(--ornament-b) 55%, transparent 80%);
  }

  /* wordmark */
  .wordmark {
    display: flex;
    align-items: center;
    gap: 12px;
  }
  .wordmark__dot {
    width: 10px;
    height: 10px;
    border-radius: 50%;
    background: var(--ink);
  }
  .wordmark__text {
    text-align: center;
    font-size: 13px;
    letter-spacing: 0.32em;
    line-height: 1.5;
  }

  /* appointment side */
  .appointment .wordmark {
    position: absolute;
    top: 58px;
    left: 170px;
  }
  .appointment__fields {
    position: absolute;
    top: 130px;
    left: 40px;
    width: 440px;
    font-size: 13px;
    letter-spacing: 0.04em;
  }
  .field {
    display: flex;
    align-items: flex-end;
    gap: 6px;
    margin-bottom: 22px;
  }
  .field__line {
    flex: 1;
    border-bottom: 1px solid var(--rule);
    height: 1px;
    margin-bottom: 3px;
  }
  .appointment__web {
    position: absolute;
    left: 40px;
    bottom: 34px;
    font-size: 11px;
    letter-spacing: 0.04em;
  }

  /* contact side */
  .contact__body {
    position: absolute;
    inset: 0;
    display: flex;
    flex-direction: column;
    align-items: center;
    justify-content: center;
    text-align: center;
  }
  .contact .wordmark { margin-bottom: 14px; }
  .contact__name {
    font-size: 16px;
    letter-spacing: 0.06em;
    margin-bottom: 10px;
  }
  .contact__details {
    list-style: none;
    font-size: 11.5px;
    letter-spacing: 0.04em;
    line-height: 1.75;
  }
</style>
</head>
<body>
<main class="canvas">

  <article class="card appointment">
    <div class="ornament ornament--top-left" role="img" aria-label="Pale silver flourish ornament"></div>
    <div class="ornament ornament--bottom-right" role="img" aria-label="Pale silver flourish ornament"></div>
    <div class="wordmark">
      <span class="wordmark__dot"></span>
      <p class="wordmark__text">Marcus Dell's<br>Salon</p>
    </div>
    <div class="appointment__fields">
      <div class="field"><span>Name</span><span class="field__line"></span></div>
      <div class="field"><span>Date</span><span class="field__line"></span><span>Time</span><span class="field__line"></span></div>
    </div>
    <p class="appointment__web">www.marcusdellsalon.example</p>
  </article>

  <article class="card contact">
    <div class="ornament ornament--top-left" role="img" aria-label="Pale silver flourish ornament"></div>
    <div class="ornament ornament--bottom-right" role="img" aria-label="Pale silver flourish ornament"></div>
    <div class="contact__body">
      <div class="wordmark">
        <span class="wordmark__dot"></span>
        <p class="wordmark__text">Marcus Dell's<br>Salon</p>
      </div>
      <p class="contact__name">Marcus Dell</p>
      <ul class="contact__details">
        <li>Phone: 212-386-7714</li>
        <li>Email: info@marcusdellsalon.example</li>
        <li>www.marcusdellsalon.example</li>
        <li>748 E. 29th Street, New York NY 10016</li>
      </ul>
    </div>
  </article>

</main>
</body>
</html>
```